Letterhead & Business Card Design Project

Use existing logo to create a new letterhead and business card design. Looking for something clean modern using color options of black, white and gray. The green from the logo may be used lightly as an accent color.

Target Market(s)

Professional business people

Industry/Entity Type

Business

Requirements
Must have
• Business card with front and back design using existing logo.
Nice to have
• Professional presentation
Clean look
Should not have
• No oil rigs, pumpjacks or clip art.

```html
<!DOCTYPE html>
<html lang="en">
<head>
<meta charset="utf-8">
<title>Halvern Resources — Business Card</title>
<link rel="stylesheet" href="https://fonts.googleapis.com/css2?family=Open+Sans:wght@400;600&display=swap">
<style>
  :root {
    --stage: #e4e4e4;
    --paper: #f6f6f6;
    --ink: #141414;
    --accent: #1fa336;
    --band: #111111;
  }
  * { margin: 0; padding: 0; box-sizing: border-box; }
  html, body { width: 1200px; height: 720px; overflow: hidden; }
  body {
    background: var(--stage);
    font-family: "Open Sans", "Segoe UI", sans-serif;
    color: var(--ink);
    display: flex;
    align-items: center;
    justify-content: center;
    gap: 44px;
  }
  .card {
    position: relative;
    width: 525px;
    height: 300px;
    background: var(--paper);
    box-shadow: 0 6px 18px rgba(0,0,0,0.16);
    overflow: hidden;
  }
  .brand-name {
    font-weight: 400;
    color: var(--ink);
    letter-spacing: 0.12em;
    text-transform: uppercase;
    white-space: nowrap;
  }
  .card-back { display: flex; align-items: center; justify-content: center; }
  .card-back .brand-name { font-size: 34px; }

  .card-front .brand-name {
    position: absolute;
    left: 48px;
    top: 78px;
    font-size: 24px;
    line-height: 1.2;
  }
  .brand-line { display: block; }
  .contact {
    position: absolute;
    left: 300px;
    top: 122px;
  }
  .person-name { font-size: 19px; font-weight: 600; line-height: 1.2; }
  .person-role { font-size: 16px; color: var(--accent); line-height: 1.3; margin-bottom: 12px; }
  .contact-list { list-style: none; }
  .contact-item {
    display: flex;
    align-items: center;
    gap: 8px;
    font-size: 14.5px;
    line-height: 1.55;
  }
  .contact-icon { width: 13px; height: 13px; flex: none; fill: var(--accent); }
  .card-band {
    position: absolute;
    left: 0; bottom: 0;
    width: 100%;
    height: 10px;
  }
</style>
</head>
<body>
  <section class="card card-back" aria-label="Business card back">
    <span class="brand-name">Halvern Resources</span>
  </section>

  <section class="card card-front" aria-label="Business card front">
    <span class="brand-name">
      <span class="brand-line">Halvern</span>
      <span class="brand-line">Resources</span>
    </span>

    <div class="contact">
      <p class="person-name">John Doe</p>
      <p class="person-role">Director</p>
      <ul class="contact-list">
        <li class="contact-item">
          <svg class="contact-icon" viewBox="0 0 24 24" aria-hidden="true"><path d="M6.6 10.8a15.1 15.1 0 0 0 6.6 6.6l2.2-2.2a1 1 0 0 1 1-.25 11.4 11.4 0 0 0 3.6.57 1 1 0 0 1 1 1V20a1 1 0 0 1-1 1A17 17 0 0 1 3 4a1 1 0 0 1 1-1h3.5a1 1 0 0 1 1 1c0 1.25.2 2.45.57 3.57a1 1 0 0 1-.25 1z"/></svg>
          <span>123-456-7890</span>
        </li>
        <li class="contact-item">
          <svg class="contact-icon" viewBox="0 0 24 24" aria-hidden="true"><path d="M2 5h20v14H2z M2 5l10 8 10-8"/></svg>
          <span>info@halvern.com</span>
        </li>
        <li class="contact-item">
          <svg class="contact-icon" viewBox="0 0 24 24" aria-hidden="true"><path d="M12 2a7 7 0 0 0-7 7c0 5.2 7 13 7 13s7-7.8 7-13a7 7 0 0 0-7-7zm0 9.5A2.5 2.5 0 1 1 12 6.5a2.5 2.5 0 0 1 0 5z"/></svg>
          <span>www.halvern.com</span>
        </li>
      </ul>
    </div>

    <svg class="card-band" viewBox="0 0 525 10" preserveAspectRatio="none" aria-hidden="true">
      <rect x="0" y="0" width="525" height="10" fill="var(--band)"/>
      <path d="M400 10 C410 0 415 0 430 0 L525 0 L525 10 Z" fill="var(--accent)"/>
    </svg>
  </section>
</body>
</html>
```